Dentistry on Brackwell Marketing Brochure

I require a brochure to market our practice and to send to new patients after they have made initial phone contact, in our 'new patient package' .
My preference is for a double sided A4 trifold brochure.
Please find attached the style guide and information to be included.
Also, please visit our website at www.dentistryonbrackwell.com.au to get an idea of our brand- we prefer a clean, fresh look that still conveys warmth and professionalism.
The images from our website can be used for the brochure.
Please include the map attached.
Industry/Entity Type
Marketing
Look and feel
Each slider illustrates characteristics of the customer's brand and the style your logo design should communicate.

```html
<!DOCTYPE html>
<html lang="en">
<head>
<meta charset="utf-8">
<title>Dentistry on Brackwell – Trifold Brochure</title>
<link href="https://fonts.googleapis.com/css2?family=Open+Sans:ital,wght@0,400;0,600;0,700;1,400&family=Libre+Baskerville:ital@1&display=swap" rel="stylesheet">
<style>
  :root {
    --backdrop: #a9aeab;
    --lime: #cdcb12;
    --slate: #5e6266;
    --paper: #ffffff;
    --ink: #1d1d1d;
    --soft: #eeeeec;
  }
  * { box-sizing: border-box; margin: 0; padding: 0; }
  html, body { width: 1200px; height: 1000px; overflow: hidden; }
  body {
    background: var(--backdrop);
    font-family: "Open Sans", Arial, sans-serif;
    color: var(--ink);
    position: relative;
  }
  .brochure {
    position: absolute; left: 60px; top: 118px;
    width: 1080px; height: 764px;
    display: flex; background: var(--paper);
    box-shadow: 0 6px 18px rgba(0,0,0,.18);
  }
  .panel { width: 360px; height: 100%; position: relative; overflow: hidden; }

  /* Left panel */
  .panel--info { display: flex; flex-direction: column; }
  .hygiene {
    background: var(--lime); color: #fff;
    height: 584px; padding: 34px 28px 0 30px;
  }
  .hygiene h2 { font-size: 16px; font-weight: 700; margin-bottom: 14px; }
  .hygiene p { font-size: 11.8px; line-height: 17.2px; margin-bottom: 10px; text-align: justify; }
  .payment {
    flex: 1; background: var(--slate); color: #fff;
    padding: 30px 30px 0 40px; position: relative;
  }
  .payment .rule { position: absolute; left: 0; top: 0; width: 360px; height: 16px; }
  .payment h2 { font-size: 16px; font-weight: 700; color: var(--lime); margin-bottom: 8px; }
  .payment .subhead { color: var(--lime); font-size: 12px; margin-top: 2px; }
  .payment .grid { display: grid; grid-template-columns: 90px 1fr; font-size: 12px; line-height: 19px; }
  .payment .plain { font-size: 12px; line-height: 19px; }

  /* Middle panel */
  .building-photo {
    height: 176px;
    background: linear-gradient(180deg, #30456d 0%, #6d7f98 45%, #b5a690 75%, #5d6a52 100%);
  }
  .map {
    margin: 14px 30px 0; height: 262px;
    background: linear-gradient(180deg, #f6f6f4, #ececea);
    border: 1px solid #e2e2df;
  }
  .hours { text-align: right; padding: 26px 30px 0 0; font-size: 11.5px; line-height: 15px; }
  .hours h3 { font-size: 12px; font-weight: 700; }
  .hours .row span { font-weight: 700; }
  .hours .note { margin-top: 6px; font-size: 11px; }
  .parking { text-align: center; font-size: 10.5px; font-weight: 700; line-height: 14px; margin: 26px 0 0 120px; width: 180px; }
  .contact { text-align: right; padding: 24px 30px 0 0; font-size: 11.5px; line-height: 14.5px; }
  .contact h3 { font-size: 15px; font-weight: 700; margin-bottom: 2px; }
  .contact b { font-weight: 700; }

  /* Right panel (cover) */
  .brand { display: flex; align-items: center; justify-content: center; gap: 10px; padding-top: 66px; }
  .brand .mark { width: 14px; height: 14px; background: var(--lime); }
  .brand .name { font-size: 22px; font-weight: 400; color: var(--ink); }
  .tagline {
    font-family: "Libre Baskerville", Georgia, serif; font-style: italic;
    text-align: right; padding: 82px 28px 0 0;
  }
  .tagline .lead { color: var(--lime); font-size: 24px; letter-spacing: 4px; }
  .tagline .sub { color: #5a5a5a; font-size: 15px; letter-spacing: 2.4px; margin-top: 2px; }
  .cover-photo {
    position: absolute; left: 0; right: 0; bottom: 0; height: 400px;
    background: linear-gradient(160deg, #f1eeea 0%, #dcc0a6 35%, #a9805f 65%, #e9e3dc 100%);
  }
</style>
</head>
<body>
  <div class="brochure">
    <section class="panel panel--info">
      <div class="hygiene">
        <h2>Hygiene Maintenance</h2>
        <p>We have a strong focus on regular hygiene maintenance for all our patients and believe prevention of dental disease is smarter and more economical than treatment. There is a growing body of evidence highlighting the relationship between oral disease and systemic diseases such as cardiovascular disease, diabetes, arthritis and sleep apnoea.</p>
        <p>Emerging evidence suggests that improving oral health can actually lower your risk of some systemic diseases. We believe this increases the importance of maintaining optimum oral health, as it's not just for your teeth and gums, but for the benefit of your whole body.</p>
        <p>Your hygiene maintenance appointments are performed by a hygienist, practitioners who are qualified specifically in the prevention of dental disease. To save you time, these appointments are typically combined with your dental examination.</p>
        <p>Most people require a hygiene appointment every six months to maintain optimal oral health, however your hygienist will assess how often you should attend based on your needs. People with certain dental and health conditions may need to attend more frequently. As well as the benefits to your mouth and your body, your teeth will feel fantastic!</p>
      </div>
      <div class="payment">
        <svg class="rule" viewBox="0 0 360 16" aria-hidden="true"><path d="M0 14 Q180 -2 360 4" fill="none" stroke="#fff" stroke-width="2"/></svg>
        <h2>Payment options</h2>
        <div class="subhead">Electronic ClaimPoint facilities available</div>
        <div class="grid"><span>Card terminal</span><span>Debit and credit cards</span><span>Cash</span><span>Cheque</span></div>
        <div class="subhead">Finance options available</div>
        <div class="plain">DVA patients welcome<br>CDBS patients welcome</div>
      </div>
    </section>

    <section class="panel panel--visit">
      <div class="building-photo" role="img" aria-label="Photograph of the practice building exterior at dusk"></div>
      <div class="map" role="img" aria-label="Street map showing the practice location and car parks"></div>
      <div class="hours">
        <h3>Opening Hours:</h3>
        <div class="row"><span>Monday - Friday</span> 8:30am - 5:30pm</div>
        <div class="row"><span>Saturday</span> 8:30am - 12:30pm</div>
        <div class="note">Urgent care appointments available each weekday.</div>
      </div>
      <div class="parking">Easy car parking available at the rear of the building</div>
      <div class="contact">
        <h3>Contact Us</h3>
        <div><b>Phone:</b> +61 8 5550 1427</div>
        <div><b>Fax:</b> 08 5550 1428</div>
        <div><b>Email:</b> smile@dentistryonbrackwell.com.au</div>
        <div><b>Website:</b> www.dentistryonbrackwell.com.au</div>
      </div>
    </section>

    <section class="panel panel--cover">
      <div class="brand"><span class="mark"></span><span class="name">Dentistry on Brackwell</span></div>
      <div class="tagline">
        <div class="lead">Quality care</div>
        <div class="sub">for every individual</div>
      </div>
      <div class="cover-photo" role="img" aria-label="Photograph of a smiling young girl with pigtails"></div>
    </section>
  </div>
</body>
</html>
```